Website Landing Page for Brightfall Systems

Create a custom designed website landing page for our business. Looking for a professional upscale design that incorporates our logo and logo colors into the theme. I want a standard fixed frame website, not a constant scrolling format that seems to be the trend. To start with I'm looking for more of the graphic design part, maybe a concept or theme, I don't expect to see a finished project. Not interested in generic templates or layouts.

The name of our company is Brightfall Systems and I've attached our logo below. I'd like to have the web page have the same look and feel of our logo, as well as the colors. Our company, Brightfall Systems does system design, installation, and programming, of residential and commercial Audio/Video and Automation systems. We do home theaters, lighting and building automation, video conferencing systems, security camera installations, conference rooms, projectors, distributed audio systems, and similar Technology projects. This will be a professional services/informational website. We will not sell products on this website. This website will be used to advertise our company and communicate our services to prospective customers. Having a well designed, professional and clean website is one way we want to distinguish our company from the competition.

Here are some examples of what I consider a professional well designed website
http://www.qorlamstudio.com/Work/

Last year we had our tradlo store designed (with PixelMarket) and I'm really happy with the way it turned out. You can see it at www.HolvenGearDepot.com I consider this to be a great design and looking for the same level of quality with this new website. However, do not copy or use any part of this design in this new project. This tradlo store is completely separate from our other company Brightfall Systems. I only mention this tradlo store an an example of good work.

Reason: Still going through designs.

Reason: Still working on project and have not had time to review all designs and request revisions.

Reason: Sill going through designs and requesting revisions

Reason: still going through all the submissions we received.

Target Market(s)

People interested in Audio/Video, home theaters, home automation. We do sales, system design, and programming. We typically work on larger projects with both residential and commercial customers.

Industry/Entity Type

Business

Number of Pages Required

1 page

Requirements
Must have
• Great design elements. Please use a white background. I think white goes well with our logo colors.

```html
<!DOCTYPE html>
<html lang="en">
<head>
<meta charset="utf-8">
<title>Brightfall Systems</title>
<link rel="stylesheet" href="https://fonts.googleapis.com/css2?family=Open+Sans:wght@300;400;600;700&display=swap">
<style>
:root{
  --blue:#3a7bc8;
  --blue-light:#36b6e6;
  --blue-dark:#2f67b3;
  --green:#8dc63f;
  --green-dark:#6fae2a;
  --text:#7a7a7a;
  --heading:#333;
  --line:#d9d9d9;
  --white:#fff;
}
*{box-sizing:border-box;margin:0;padding:0}
html,body{width:1200px;height:2267px;overflow:hidden;background:var(--white)}
body{position:relative;font-family:"Open Sans",Arial,sans-serif;color:var(--text)}
.abs{position:absolute}

/* header */
.site-header{position:absolute;left:0;top:0;width:1200px;height:103px;border-bottom:3px solid #e6e6e6;background:var(--white)}
.brand{position:absolute;left:246px;top:26px;display:flex;align-items:center;gap:8px}
.brand-dot{width:30px;height:30px;border-radius:50%;background:var(--blue)}
.brand-name{font-size:18px;font-weight:700;color:var(--green);line-height:1.05;width:110px}
.top-social{position:absolute;left:615px;top:21px;display:flex;gap:5px}
.top-social span{width:17px;height:17px;border-radius:50%;background:var(--green)}
.top-contact{position:absolute;top:21px;font-size:11px;color:var(--text);display:flex;align-items:center;gap:8px}
.main-nav{position:absolute;top:72px;left:0;width:1200px;font-size:10px;color:#555}
.main-nav a{position:absolute;color:#555;text-decoration:none}
.main-nav a.active{color:var(--green);font-weight:600}
.nav-underline{position:absolute;left:668px;top:100px;width:38px;height:3px;background:var(--green)}

/* hero */
.hero{position:absolute;left:0;top:103px;width:1200px;height:307px;z-index:2;
  background:linear-gradient(90deg,#f2f0ee 0,#e9e6e2 12%,#6e4a36 20%,#5b3b2a 50%,#6e4a36 80%,#e9e6e2 88%,#f2f0ee 100%)}
.hero-title{position:absolute;left:0;width:1200px;top:206px;text-align:center;color:var(--white);font-size:29px;font-weight:300;line-height:1}
.hero-title strong{display:block;font-weight:600;font-size:26px;margin-top:4px}
.hero-dots{position:absolute;left:585px;top:281px;display:flex;gap:4px}
.hero-dots span{width:7px;height:7px;border-radius:50%;background:#bbb}
.hero-dots span:first-child{background:var(--white)}

/* about */
.about-title{left:248px;top:444px;font-size:24px;font-weight:600;color:var(--blue)}
.about-text{left:248px;top:493px;width:240px;font-size:10.5px;line-height:15px;font-weight:300;text-align:justify}
.btn{display:inline-block;background:var(--green);color:var(--white);font-weight:700;font-size:10.5px;text-align:center}
.read-more{left:248px;top:718px;width:84px;height:26px;line-height:26px}
.about-visual{left:532px;top:327px;z-index:1}

/* section headings */
.section-title{position:absolute;left:0;width:1200px;text-align:center;font-size:29px;line-height:38px;color:var(--blue);font-weight:400}
.section-title strong{font-weight:700}

/* services */
.service{position:absolute;width:220px;text-align:center}
.service svg{display:block;margin:0 auto}
.service h3{font-size:18px;font-weight:400;color:var(--blue);line-height:23px;margin-top:12px}
.service h3 strong{font-weight:700}
.service p{font-size:11px;line-height:15px;width:185px;margin:6px auto 0}

/* what we do */
.feature{position:absolute;width:336px;height:336px}
.feature-body{position:absolute;left:53px;top:106px;width:230px;text-align:center}
.feature-body h3{font-size:19px;font-weight:400;color:var(--blue);line-height:26px}
.feature-body p{font-size:11px;line-height:15.6px;margin-top:2px}
.dots{position:absolute;display:flex;gap:4px}
.dots span{width:9px;height:9px;border-radius:50%;background:#9dbbe3}
.dots span:first-child{background:var(--blue)}

/* smarter homes */
.arrow-btn{position:absolute;top:1589px}
.project{position:absolute;top:1642px;width:228px}
.project-photo{height:139px;border-radius:3px}
.project h3{font-size:19px;font-weight:400;color:var(--blue);margin-top:10px;line-height:26px}
.project p{font-size:11px;line-height:15.5px;margin-top:4px;width:226px}

/* footer */
.footer-rule{left:248px;top:1917px;width:702px;height:1px;background:var(--line)}
.footer-brand{left:248px;top:1941px;width:186px;text-align:center}
.footer-brand .brand-dot{width:106px;height:106px;border-radius:50%;border:10px solid var(--blue);background:none;margin:0 auto}
.footer-brand .brand-name{width:auto;font-size:27px;margin-top:14px;line-height:1.15}
.footer-social{left:249px;top:2138px;display:flex;gap:9px}
.footer-social span{width:40px;height:40px;border-radius:50%;background:var(--green)}
.contact-item{position:absolute;left:474px;display:flex;gap:10px}
.contact-item small{display:block;font-size:9px;color:#555}
.contact-item b{display:block;font-size:13px;color:#444;line-height:16px}
.callback{left:680px;top:1936px;width:272px}
.callback h4{font-size:14px;font-weight:400;color:#444;margin-bottom:8px}
.field{height:25px;border:1px solid #e2e2e2;border-radius:3px;margin-bottom:5px;font-size:9.5px;line-height:23px;padding-left:8px;color:#777}
.field.message{height:52px}
.submit{width:145px;height:27px;line-height:27px;margin-top:5px}
.copyright{left:248px;top:2218px;font-size:9px;color:#444}
</style>
</head>
<body>

<header class="site-header">
  <div class="brand"><span class="brand-dot"></span><span class="brand-name">BRIGHTFALL SYSTEMS</span></div>
  <div class="top-social"><span></span><span></span><span></span><span></span></div>
  <div class="top-contact" style="left:725px">
    <svg width="16" height="16" viewBox="0 0 24 24"><path d="M6 3l3 4-2 2c1 3 4 6 7 7l2-2 4 3-2 4C10 21 3 14 3 5z" fill="none" stroke="#8dc63f" stroke-width="2"/></svg>+000 000 0000
  </div>
  <div class="top-contact" style="left:844px">
    <svg width="17" height="12" viewBox="0 0 17 12"><rect x="1" y="1" width="15" height="10" fill="none" stroke="#8dc63f" stroke-width="1.6"/><path d="M1 1l7.5 6L16 1" fill="none" stroke="#8dc63f" stroke-width="1.6"/></svg>info@brightfallsys.com
  </div>
  <nav class="main-nav">
    <a class="active" style="left:676px">Home</a>
    <a style="left:730px">About</a>
    <a style="left:781px">Services</a>
    <a style="left:842px">Audio/video</a>
    <a style="left:919px">Contact</a>
  </nav>
  <span class="nav-underline"></span>
</header>

<section class="hero" role="img" aria-label="Photo of a modern boardroom with wood-panelled wall, wall screen and black chairs">
  <h1 class="hero-title">Business Brightfall<strong>Systems</strong></h1>
  <div class="hero-dots"><span></span><span></span><span></span></div>
</section>

<h2 class="abs about-title">Brightfall Systems.</h2>
<p class="abs about-text">Lorem Ipsum is simply dummy text of the printing and typesetting industry. Lorem Ipsum has been the industry's standard dummy text ever since the 1500s, when an unknown printer took a galley of type and scrambled it to make a type specimen book. Lorem Ipsum is simply dummy text of the printing and typesetting industry. Lorem Ipsum has been the industry's standard dummy text ever since the 1500s, when an unknown printer took a galley of type and scrambled it to make a type specimen book.</p>
<span class="abs btn read-more">Read More</span>

<svg class="abs about-visual" width="418" height="418" viewBox="0 0 420 420">
  <defs>
    <linearGradient id="ringGrad" x1="0" y1="0" x2="1" y2="1">
      <stop offset="0" stop-color="#2f67b3"/><stop offset=".55" stop-color="#3a7bc8"/><stop offset=".8" stop-color="#36b6e6"/><stop offset="1" stop-color="#2f67b3"/>
    </linearGradient>
    <linearGradient id="hallGrad" x1="0" y1="0" x2="0" y2="1">
      <stop offset="0" stop-color="#6f7c8a"/><stop offset=".5" stop-color="#3e4650"/><stop offset="1" stop-color="#8e9096"/>
    </linearGradient>
  </defs>
  <circle cx="210" cy="210" r="210" fill="url(#ringGrad)"/>
  <circle cx="210" cy="210" r="178" fill="url(#hallGrad)" role="img" aria-label="Photo of an auditorium with rows of seats and a projection screen"/>
</svg>

<h2 class="section-title" style="top:762px">Our <strong>Services</strong></h2>

<svg width="0" height="0" style="position:absolute">
  <defs>
    <linearGradient id="svcRing" x1="0" y1="0" x2="1" y2="1">
      <stop offset="0" stop-color="#2f67b3"/><stop offset=".7" stop-color="#3a7bc8"/><stop offset="1" stop-color="#36b6e6"/>
    </linearGradient>
  </defs>
</svg>

<div class="service" style="left:231px;top:820px">
  <svg width="184" height="184" viewBox="0 0 184 184">
    <circle cx="92" cy="92" r="92" fill="url(#svcRing)"/><circle cx="92" cy="92" r="80" fill="#fff"/><circle cx="92" cy="92" r="73" fill="#8dc63f"/>
    <path d="M160 55a80 80 0 0 1 5 12" stroke="#8dc63f" stroke-width="9" fill="none"/>
    <path d="M24 129a80 80 0 0 1-5-12" stroke="#8dc63f" stroke-width="9" fill="none"/>
    <g fill="none" stroke="#fff" stroke-width="3">
      <rect x="50" y="58" width="12" height="68"/><rect x="122" y="58" width="12" height="68"/>
      <rect x="70" y="66" width="44" height="28"/><rect x="72" y="102" width="40" height="14"/><circle cx="82" cy="109" r="3"/>
    </g>
  </svg>
  <h3>Full Home <strong>Cinema</strong></h3>
  <p>Lorem Ipsum has been the industry's standard dummy text ever since the 1500s, when an</p>
</div>

<div class="service" style="left:490px;top:820px">
  <svg width="184" height="184" viewBox="0 0 184 184">
    <circle cx="92" cy="92" r="92" fill="url(#svcRing)"/><circle cx="92" cy="92" r="80" fill="#fff"/><circle cx="92" cy="92" r="73" fill="#8dc63f"/>
    <path d="M160 55a80 80 0 0 1 5 12" stroke="#8dc63f" stroke-width="9" fill="none"/>
    <path d="M24 129a80 80 0 0 1-5-12" stroke="#8dc63f" stroke-width="9" fill="none"/>
    <g fill="none" stroke="#fff" stroke-width="3" stroke-linejoin="round">
      <path d="M92 58l36 20-36 20-36-20z"/><path d="M56 90l36 20 36-20"/><path d="M56 102l36 20 36-20"/>
    </g>
  </svg>
  <h3>Interior Design &amp;<br><strong>Showhouses</strong></h3>
  <p>Lorem Ipsum has been the industry's standard dummy text</p>
</div>

<div class="service" style="left:750px;top:820px">
  <svg width="184" height="184" viewBox="0 0 184 184">
    <circle cx="92" cy="92" r="92" fill="url(#svcRing)"/><circle cx="92" cy="92" r="80" fill="#fff"/><circle cx="92" cy="92" r="73" fill="#8dc63f"/>
    <path d="M160 55a80 80 0 0 1 5 12" stroke="#8dc63f" stroke-width="9" fill="none"/>
    <path d="M24 129a80 80 0 0 1-5-12" stroke="#8dc63f" stroke-width="9" fill="none"/>
    <g fill="none" stroke="#fff" stroke-width="3" stroke-linejoin="round">
      <path d="M58 80h14l20-18v60L72 104H58z"/><path d="M100 78a18 18 0 0 1 0 28"/><path d="M108 68a30 30 0 0 1 0 48"/>
    </g>
  </svg>
  <h3>Multi-Room <strong>Music<br>Systems</strong></h3>
  <p>Lorem Ipsum has been the industry's standard dummy text</p>
</div>

<h2 class="section-title" style="top:1144px">What <strong>We Do</strong></h2>

<div class="feature" style="left:248px;top:1201px">
  <svg width="336" height="336" viewBox="0 0 340 340">
    <circle cx="170" cy="170" r="168" fill="url(#svcRing)"/>
    <circle cx="170" cy="170" r="136" fill="#fff"/>
    <circle cx="170" cy="170" r="128" fill="#fafafa" stroke="#ececec" stroke-width="4"/>
    <path d="M285 105a136 136 0 0 1 9 25" stroke="#8dc63f" stroke-width="14" fill="none"/>
    <path d="M55 235a136 136 0 0 1-9-25" stroke="#8dc63f" stroke-width="14" fill="none"/>
  </svg>
  <div class="feature-body"><h3>Home Entertainment</h3><p>Lorem Ipsum has been the industry's standard dummy text ever since the 1500s, when an unknown printer took a galley of type and scrambled it to make a type specimen book.</p></div>
</div>

<div class="feature" style="left:616px;top:1201px">
  <svg width="336" height="336" viewBox="0 0 340 340">
    <circle cx="170" cy="170" r="168" fill="url(#svcRing)"/>
    <circle cx="170" cy="170" r="136" fill="#fff"/>
    <circle cx="170" cy="170" r="128" fill="#fafafa" stroke="#ececec" stroke-width="4"/>
    <path d="M285 105a136 136 0 0 1 9 25" stroke="#8dc63f" stroke-width="14" fill="none"/>
    <path d="M55 235a136 136 0 0 1-9-25" stroke="#8dc63f" stroke-width="14" fill="none"/>
  </svg>
  <div class="feature-body"><h3>Home Automation</h3><p>Lorem Ipsum has been the industry's standard dummy text ever since the 1500s, when an unknown printer took a galley of type and scrambled it to make a type specimen book.</p></div>
</div>

<div class="dots" style="left:580px;top:1527px"><span></span><span></span><span></span></div>

<svg class="arrow-btn" style="left:248px" width="28" height="28" viewBox="0 0 28 28"><circle cx="14" cy="14" r="14" fill="#3a7bc8"/><path d="M20 14H8m5-5l-5 5 5 5" stroke="#fff" stroke-width="2" fill="none"/></svg>
<h2 class="section-title" style="top:1584px">Smarter <strong>Homes</strong></h2>
<svg class="arrow-btn" style="left:923px" width="28" height="28" viewBox="0 0 28 28"><circle cx="14" cy="14" r="14" fill="#3a7bc8"/><path d="M8 14h12m-5-5l5 5-5 5" stroke="#fff" stroke-width="2" fill="none"/></svg>

<article class="project" style="left:248px">
  <div class="project-photo" role="img" aria-label="Photo of a warmly lit hotel lobby" style="background:linear-gradient(180deg,#8a6a3a,#c9a266 55%,#6b4a26)"></div>
  <h3>Hotel lobby</h3>
  <p>Lorem Ipsum has been the industry's standard dummy text ever since the 1500s, when an unknown printer took a galley of</p>
</article>
<article class="project" style="left:485px">
  <div class="project-photo" role="img" aria-label="Photo of a modern lounge reception area" style="background:linear-gradient(180deg,#3a2a24,#7a4a36 55%,#c07a4a)"></div>
  <h3>Lounge</h3>
  <p>Lorem Ipsum has been the industry's standard dummy text ever since the 1500s, when an unknown printer took a galley of</p>
</article>
<article class="project" style="left:724px">
  <div class="project-photo" role="img" aria-label="Photo of glass office towers against a blue sky" style="background:linear-gradient(180deg,#4d86d6,#2f5fa8 60%,#7aa7df)"></div>
  <h3>Buildings</h3>
  <p>Lorem Ipsum has been the industry's standard dummy text ever since the 1500s, when an unknown printer took a galley of</p>
</article>

<div class="abs footer-rule"></div>

<div class="abs footer-brand"><span class="brand-dot" style="display:block"></span><div class="brand-name">BRIGHTFALL<br>SYSTEMS</div></div>
<div class="abs footer-social"><span></span><span></span><span></span><span></span></div>

<div class="contact-item" style="top:1960px">
  <svg width="24" height="24" viewBox="0 0 24 24"><path d="M6 3l3 4-2 2c1 3 4 6 7 7l2-2 4 3-2 4C10 21 3 14 3 5z" fill="none" stroke="#8dc63f" stroke-width="1.6"/></svg>
  <div><small>Call Us Today!</small><b>+00 (0) 000 0000</b></div>
</div>
<div class="contact-item" style="top:2012px">
  <svg width="26" height="20" viewBox="0 0 26 20"><rect x="1" y="1" width="24" height="18" fill="none" stroke="#8dc63f" stroke-width="1.6"/><path d="M1 1l12 10L25 1M1 19l9-8m15 8l-9-8" fill="none" stroke="#8dc63f" stroke-width="1.6"/></svg>
  <div><small>Email</small><b>info@brightfallsys.com</b></div>
</div>
<div class="contact-item" style="top:2062px">
  <svg width="24" height="30" viewBox="0 0 24 30"><path d="M12 29S2 17 2 11a10 10 0 0 1 20 0c0 6-10 18-10 18z" fill="none" stroke="#8dc63f" stroke-width="1.6"/><circle cx="12" cy="11" r="4" fill="none" stroke="#8dc63f" stroke-width="1.6"/></svg>
  <div><small>Address City</small><b>ABC Street, City<br>Lorem Ipsum is<br>simply dummy.</b></div>
</div>

<form class="abs callback">
  <h4>Request a Callback</h4>
  <div class="field">Name</div>
  <div class="field">Email</div>
  <div class="field">Your telephone</div>
  <div class="field">Your Mobile</div>
  <div class="field message">Message</div>
  <span class="btn submit">Submit Your Message</span>
</form>

<p class="abs copyright">© 2017 Brightfall Systems. All Rights Reserved.</p>

</body>
</html>
```